New document sharing business needs snazzy icons

We need two icons designed for a new document sharing business based in Brisbane, Australia. Users of the website can download high quality document templates and examples, or upload content to share with others.
We need two icons to go on the home page that draws attention to the two main functions of the website (download and share). These icons need to be a little different, but consistent in size and general appearance. These icons will hyperlink to the "download" and "upload" pages of the website.
The first icon needs to have the word "Download" as the dominant word. Under or beside this word the following words need to appear: "search and download documents" in smaller writing. The image needs to portray a professional, elegant look whilst being visually appealing. This icon may use the down arrow or some variation to depict the downloading of a document.
The second icon needs to have the word "Share" as the dominant word. Under or beside this word the following words need to appear: "upload your documents to get free downloads" in smaller writing. This icon may use the up arrow or some variation to depict the sharing or uploading of documents.
I would expect that both icons may use different (but complimentary) colours, and be of the same overall size and structure.
Customers are business managers and executives.
Business

```html
<!DOCTYPE html>
<html lang="en">
<head>
<meta charset="UTF-8">
<title>Download and Share Icons</title>
<link rel="stylesheet" href="https://fonts.googleapis.com/css2?family=Open+Sans:wght@600&family=Source+Code+Pro:wght@700&display=swap">
<style>
  :root {
    --navy: #000066;
    --aqua: #99ffff;
    --forest: #003333;
    --lime: #ccff66;
    --white: #ffffff;
  }
  html, body {
    margin: 0;
    padding: 0;
    width: 1200px;
    height: 295px;
    overflow: hidden;
    background: var(--white);
  }
  .canvas {
    position: relative;
    width: 1200px;
    height: 295px;
  }
  .action-card {
    position: absolute;
    display: flex;
    flex-direction: column;
    overflow: hidden;
    text-decoration: none;
  }
  .action-card--download {
    left: 0;
    top: 0;
    width: 583px;
    height: 292px;
    border-radius: 0 0 62px 62px;
    background: var(--aqua);
  }
  .action-card--share {
    left: 613px;
    top: 2px;
    width: 583px;
    height: 285px;
    border-radius: 6px 6px 62px 62px;
    background: var(--lime);
  }
  .action-card__title {
    margin: 0;
    display: flex;
    align-items: center;
    justify-content: center;
    color: var(--white);
    font-family: "Open Sans", sans-serif;
    font-weight: 600;
    line-height: 1;
    letter-spacing: 0;
  }
  .action-card--download .action-card__title {
    height: 125px;
    background: var(--navy);
    font-size: 98px;
    padding-top: 2px;
  }
  .action-card--share .action-card__title {
    height: 113px;
    background: var(--forest);
    font-size: 90px;
    padding-top: 0;
  }
  .action-card__caption {
    margin: 0;
    text-align: center;
    font-family: "Source Code Pro", monospace;
    font-weight: 700;
    white-space: nowrap;
  }
  .action-card--download .action-card__caption {
    color: var(--navy);
    font-size: 50px;
    line-height: 60px;
    padding-top: 16px;
  }
  .action-card--share .action-card__caption {
    color: var(--forest);
    font-size: 40px;
    line-height: 53px;
    padding-top: 25px;
  }
</style>
</head>
<body>
  <main class="canvas">
    <a class="action-card action-card--download" href="#download">
      <h2 class="action-card__title">DOWNLOAD</h2>
      <p class="action-card__caption">search &amp; download<br>documents</p>
    </a>
    <a class="action-card action-card--share" href="#upload">
      <h2 class="action-card__title">SHARE</h2>
      <p class="action-card__caption">upload your documents<br>to get free downloads</p>
    </a>
  </main>
</body>
</html>
```